TalvoMesh

Hey

I am involved with crowd funding, please look at one of my current sites www.pennorift.com
Work is currently under way with a new site www.talvomesh.com .wehave the basics but I am not happy with what we have so far. I need to redesign the web site but keep the concept . The cartoon pitch will be kept , along with some of the other functions which we can help you with, unless you are able to build / design something better. I liked a lot of the designs submitted for a previous crowd funning design, far better than what I currently have. To be included on this site will be links to numerous crowd funding sites which I have registered but each site will be focused on a specific topic which will be disclosed once this site is active. I intend to build all these sites through this site. Along with these sites will be a logo design for each site so plenty of work going forward. I have a logo for talvomesh already but am open for improvements and suggestions but would like to keep a map or logo of Africa included in the design. To bear in mind this is a African focused buisness which aims to help communities, employment creation, poverty alleviation and help young entrepreneurs kickstarter their buisness . I already have a group logo , which was designed on this site ( look at brelo yards competition) , I would like this logo to be used on all the site so customers and investors link the group and concept togeather. Here is the link http://www.quillmarta.co.uk/project-progress.aspx?briefId=48213 . I have removed the breloyard from the bottom of the logo and will just be using the figurines as the group logo on all web sites. There will be at least fifty related crowd fund projects linked to this site.
If any body has any questions or ideas please feel free to ask for anything you may need. Thanks to everybody who helps with this project. Warmly. Owen
Updates

Hi everyone working on my design.

The contact details to use on the site are

27 Velder Grove
Marnsdal
Cape Town 
+263745208839
+447911463052

E mail enquiries@TalvoMesh.example

There are two logos, one is the talvomesh logo and the other is my group logo which I will attach to the pitch
Good luck and thank you to everybody who is working on this web design
Warmly

Owen

Industry/Entity Type

Build

```html
<!DOCTYPE html>
<html lang="en">
<head>
<meta charset="utf-8">
<title>TalvoMesh – Crowdfunding</title>
<link rel="stylesheet" href="https://fonts.googleapis.com/css2?family=Roboto+Condensed:wght@400;700&family=Arimo:wght@400;700&display=swap">
<style>
:root{
  --green:#8cc63f;
  --green-dark:#5a9a1a;
  --green-btn:#0f9a2a;
  --lime-top:#c8e34a;
  --lime-bot:#86b81c;
  --ink:#222;
  --body:#444;
  --muted:#666;
  --blue:#1a4fb5;
  --line:#d8d8d8;
  --foot:#f0f0f0;
}
*{box-sizing:border-box;margin:0;padding:0}
html,body{width:882px;height:1200px;overflow:hidden;background:#fff}
body{position:relative;font-family:"Arimo",Arial,sans-serif;color:var(--body)}
.abs{position:absolute}
.cond{font-family:"Roboto Condensed","Arial Narrow",sans-serif}

/* header */
.band{left:0;top:68px;width:882px;height:145px;background:var(--green)}
.band-under{left:0;top:213px;width:882px;height:16px;background:#f2f2f2}
.brand{left:105px;top:60px;width:121px;height:48px;border-radius:50%;background:#fff;border:1px solid #cfd8c0;display:flex;align-items:center;justify-content:center;gap:5px;font-size:12px;color:#3a5a2a}
.brand-top{left:148px;top:14px;width:34px;height:34px;border-radius:50%;background:#7aaa3a}
.brand-dot{width:7px;height:7px;border-radius:50%;background:var(--green-dark)}
.nav{top:27px;font-size:10.5px;color:var(--ink);letter-spacing:.2px}
.nav.active{border-bottom:2px solid var(--green);padding-bottom:2px}
.mail{right:103px;top:49px;font-size:9px;color:var(--blue)}
.subnav{top:134px;font-size:11.5px;color:#1f2d10}
.field{left:440px;width:145px;height:16px;background:#fff;border:1px solid #b9d98c;font-size:8.5px;color:#333;padding:3px 4px}
.login{left:441px;top:128px;width:39px;height:16px;background:var(--green-btn);color:#fff;font-size:9px;text-align:center;line-height:16px;border-radius:2px}
.forgot{left:496px;top:133px;font-size:8.5px;color:#1f2d10}
.register{left:624px;top:84px;width:119px;height:35px;border-radius:3px;background:linear-gradient(var(--lime-top),var(--lime-bot));border:1px solid #7aa51a;color:#1e3a05;font-size:14px;text-align:center;line-height:34px}
.social-sign{left:637px;top:129px;width:94px;height:14px;background:#4a68a8;color:#fff;font-size:7px;line-height:14px;padding-left:18px;border:1px solid #2e4a88}
.social-sign::before{content:"";position:absolute;left:3px;top:2px;width:9px;height:9px;background:#fff}

.hero{left:103px;top:158px;width:676px;height:233px;background:linear-gradient(160deg,#8a7a66 0%,#5a4a3e 45%,#3a3330 100%)}
.hero-arrow{top:366px;width:19px;height:19px;border-radius:50%;background:#fff;box-shadow:0 0 2px rgba(0,0,0,.5);display:flex;align-items:center;justify-content:center}

.rules{left:103px;top:403px;width:676px;font-size:7.8px;line-height:13px;color:#555}
.rules b{font-weight:400;color:var(--blue)}
.rule-line{left:103px;top:437px;width:676px;height:4px;border-top:2px solid var(--green);border-bottom:1px solid var(--green)}

/* intro */
.intro{left:106px;top:460px;width:470px;height:225px;border:1px solid var(--line);border-radius:6px;box-shadow:0 1px 3px rgba(0,0,0,.15)}
.video{left:120px;top:473px;width:259px;height:177px;background:#111}
.video-art{left:120px;top:492px;width:259px;height:134px;background:linear-gradient(#bfc3c8,#d9dadc)}
.play{left:234px;top:538px;width:30px;height:26px;border-radius:6px;background:#1a1a1a;display:flex;align-items:center;justify-content:center}
.vbar{left:120px;top:626px;width:259px;height:24px;background:#222;color:#ccc;font-size:6.5px;padding:8px 0 0 56px}
.vtop{left:300px;top:478px;font-size:6.5px;color:#ddd}
.intro-title{left:389px;top:472px;font-size:12.5px;color:var(--ink)}
.intro-copy{left:390px;top:494px;width:180px;font-size:8px;line-height:14.4px;color:#444}
.pill{left:598px;width:118px;height:35px;border-radius:3px;background:linear-gradient(var(--lime-top),var(--lime-bot));border:1px solid #7aa51a;color:#1e3a05;font-size:14px;line-height:35px;padding-left:10px}
.side-copy{left:598px;width:180px;font-size:7.9px;line-height:13.6px;color:#555}

/* project cards */
.card-title{top:697px;font-size:11.5px;color:#4a6b14}
.card{top:716px;width:154px;height:239px;border:1px solid var(--line);box-shadow:0 6px 6px -4px rgba(0,0,0,.2)}
.card-img{position:absolute;left:8px;top:10px;width:138px;height:105px}
.card-copy{position:absolute;left:8px;top:125px;width:140px;font-size:7.9px;line-height:13.6px;color:#333}
.card-stats{position:absolute;left:0;top:184px;width:152px;height:31px;border-top:1px solid var(--line)}
.gift{position:absolute;left:7px;top:6px;width:20px;height:24px}
.count{position:absolute;left:32px;top:7px;font-size:16px;color:#1e3f8a}
.funded{position:absolute;right:4px;top:6px;text-align:right;font-size:8.3px;line-height:13.5px;color:#777}
.funded b{font-weight:400;color:#222;font-size:9px}
.card-tag{position:absolute;left:2px;top:216px;width:148px;height:20px;background:var(--green);color:#1a2a06;font-size:9.5px;line-height:20px;padding-left:5px}

/* categories */
.cat-line{left:0;top:995px;width:882px;height:1px;background:var(--line)}
.cat-btn{left:360px;top:983px;width:163px;height:24px;background:var(--green-btn);color:#fff;font-size:11px;text-align:center;line-height:24px}
.cat{font-size:9.5px;color:#444;padding-left:13px}
.cat::before{content:"";position:absolute;left:0;top:2px;width:8px;height:8px;border-radius:50%;background:#ddd;border:1px solid #bbb}

/* footer */
.foot{left:22px;top:1115px;width:860px;height:85px;background:var(--foot);border-top:1px dashed #bbb}
.badge{top:1133px;height:34px}
.soc{top:1131px;width:22px;height:22px;border-radius:2px}
.copyright{left:0;top:1181px;width:882px;text-align:center;font-size:8px;color:#333}
</style>
</head>
<body>

<!-- header -->
<div class="abs band"></div>
<div class="abs band-under"></div>
<div class="abs brand-top"></div>
<div class="abs brand"><span class="brand-dot"></span>Brelo Yards</div>

<span class="abs nav cond active" style="left:425px">BLOG</span>
<span class="abs nav cond" style="left:468px">IPO'S</span>
<span class="abs nav cond" style="left:514px">HOW IT WORKS</span>
<span class="abs nav cond" style="left:605px">ABOUT</span>
<span class="abs nav cond" style="left:660px">MY ACCOUNT</span>
<span class="abs nav cond" style="left:741px">MY CART</span>
<span class="abs mail">more@talvomesh.com</span>

<span class="abs subnav cond" style="left:103px">JOIN NOW</span>
<span class="abs subnav cond" style="left:178px">BROWSE COMPANIES</span>

<div class="abs field" style="top:83px">Username</div>
<div class="abs field" style="top:106px">Password</div>
<div class="abs login">Login</div>
<span class="abs forgot">Forgot Password?</span>
<div class="abs register cond">REGISTER NOW</div>
<div class="abs social-sign">Sign in with Frendly</div>

<div class="abs hero" role="img" aria-label="Group photo of the team standing together indoors"></div>
<div class="abs hero-arrow" style="left:726px"><svg width="6" height="8"><path d="M5 1L1 4l4 3" fill="none" stroke="#333" stroke-width="1.5"/></svg></div>
<div class="abs hero-arrow" style="left:753px"><svg width="6" height="8"><path d="M1 1l4 3-4 3" fill="none" stroke="#333" stroke-width="1.5"/></svg></div>

<p class="abs rules"><b>Ground rules are simple</b> ; JOIN, send us a Vidora or any other video link to any idea. It can be an idea just floating around or an idea which has already come to life. No catches, no entry fee, no award collection fee, only one entry per member.</p>
<div class="abs rule-line"></div>

<!-- intro -->
<div class="abs intro"></div>
<div class="abs video"></div>
<div class="abs video-art" role="img" aria-label="Cartoon pitch video still with dollar signs above a row of drawn people"></div>
<span class="abs vtop">Share &nbsp;&nbsp;&nbsp; ▼ More info</span>
<div class="abs play"><svg width="10" height="12"><path d="M1 1l8 5-8 5z" fill="#fff"/></svg></div>
<div class="abs vbar">0:00 / 1:25</div>
<div class="abs intro-title cond">What is Crowdfunding?</div>
<p class="abs intro-copy">Crowdfunding enables people to raise money for innovative new projects by getting like-minded individuals to pool their money to back the idea, person or business. It's a way to make things happen.</p>

<div class="abs pill cond" style="top:460px">FUND</div>
<p class="abs side-copy" style="top:500px">The elephant with no trunk. They say that a picture paints a thousand words, but no words can describe the pain, the anguish and the...</p>
<div class="abs pill cond" style="top:568px">JOIN</div>
<p class="abs side-copy" style="top:607px">The elephant with no trunk. They say that a picture paints a thousand words, but no words can describe the pain, the anguish and the...</p>

<!-- project cards -->
<div class="abs card-title cond" style="left:103px">Ut placerat nunc suscipit</div>
<div class="abs card" style="left:104px">
  <div class="card-img" role="img" aria-label="Photo of pale blue hydrangea flowers" style="background:radial-gradient(circle at 55% 45%,#b9c8d8,#3d6a2a 60%,#1f3a14)"></div>
  <p class="card-copy">Ut placerat nunc suscipit metus lacinia vel interdum tortor eleifend. Aliquam erat volutpat. Ut consectetur auctor ornare.</p>
  <div class="card-stats"><svg class="gift" viewBox="0 0 20 24"><rect x="1" y="6" width="18" height="17" fill="#e9b431"/><rect x="8" y="6" width="4" height="17" fill="#c0392b"/><rect x="1" y="6" width="18" height="4" fill="#7b5ea7"/></svg><span class="count">0</span><div class="funded">Funded $0<br><b>Goal $1,000</b></div></div>
  <div class="card-tag cond">Russia</div>
</div>

<div class="abs card-title cond" style="left:277px">Proin in ante et nulla</div>
<div class="abs card" style="left:278px">
  <div class="card-img" role="img" aria-label="Photo of penguins on ice" style="background:linear-gradient(#5b8ec8,#a9c4de 55%,#6a737d)"></div>
  <p class="card-copy">Proin in ante et nulla mollis faucibus non sit amet felis. Vestibulum ac eros risus. Nullam turpis orci, ornare vitae porta vitae...</p>
  <div class="card-stats"><svg class="gift" viewBox="0 0 20 24"><rect x="1" y="6" width="18" height="17" fill="#e9b431"/><rect x="8" y="6" width="4" height="17" fill="#c0392b"/><rect x="1" y="6" width="18" height="4" fill="#7b5ea7"/></svg><span class="count">0</span><div class="funded">Funded $0<br><b>Goal $500</b></div></div>
  <div class="card-tag cond">Middle East</div>
</div>

<div class="abs card-title cond" style="left:450px">Vestibulum sed nulla</div>
<div class="abs card" style="left:451px">
  <div class="card-img" role="img" aria-label="Photo of pale blue hydrangea flowers" style="background:radial-gradient(circle at 55% 45%,#b9c8d8,#3d6a2a 60%,#1f3a14)"></div>
  <p class="card-copy">Vestibulum sed nulla in ipsum venenatis semper. Pellentesque ut leo sed lorem lobortis semper ac ut risus...</p>
  <div class="card-stats"><svg class="gift" viewBox="0 0 20 24"><rect x="1" y="6" width="18" height="17" fill="#e9b431"/><rect x="8" y="6" width="4" height="17" fill="#c0392b"/><rect x="1" y="6" width="18" height="4" fill="#7b5ea7"/></svg><span class="count">0</span><div class="funded">Funded $0<br><b>Goal $4,000</b></div></div>
  <div class="card-tag cond">Eastern Europe</div>
</div>

<div class="abs card-title cond" style="left:623px">The elephant with no trunk</div>
<div class="abs card" style="left:625px">
  <div class="card-img" role="img" aria-label="Photo of a young elephant in grassland" style="background:linear-gradient(#8e8a7c,#9a8f78 60%,#6f7a4a)"></div>
  <p class="card-copy">The elephant with no trunk. They say that a picture paints a thousand words, but no words can describe the pain...</p>
  <div class="card-stats"><svg class="gift" viewBox="0 0 20 24"><rect x="1" y="6" width="18" height="17" fill="#e9b431"/><rect x="8" y="6" width="4" height="17" fill="#c0392b"/><rect x="1" y="6" width="18" height="4" fill="#7b5ea7"/></svg><span class="count">2</span><div class="funded">Funded $2<br><b>Goal $51</b></div></div>
  <div class="card-tag cond">Gache Gache Reserve, Zimbabwe</div>
</div>

<!-- categories -->
<div class="abs cat-line"></div>
<div class="abs cat-btn cond">BUSINESS CATEGORIES</div>
<span class="abs cat cond" style="left:104px;top:1024px">Comics</span>
<span class="abs cat cond" style="left:230px;top:1024px">Environment</span>
<span class="abs cat cond" style="left:418px;top:1024px">Fashion</span>
<span class="abs cat cond" style="left:537px;top:1024px">Film and Video</span>
<span class="abs cat cond" style="left:668px;top:1024px">Gaming</span>
<span class="abs cat cond" style="left:104px;top:1051px">Health and Fitness</span>
<span class="abs cat cond" style="left:230px;top:1053px">Internet, IT and Telecommunications</span>
<span class="abs cat cond" style="left:418px;top:1054px">Leisure and Tourism</span>
<span class="abs cat cond" style="left:537px;top:1054px">Music</span>
<span class="abs cat cond" style="left:668px;top:1054px">Professional Services</span>
<span class="abs cat cond" style="left:104px;top:1076px">Technology</span>

<!-- footer -->
<div class="abs foot"></div>
<div class="abs badge" style="left:106px;width:126px"><svg width="126" height="34"><circle cx="17" cy="17" r="16" fill="#e6a820"/><circle cx="17" cy="17" r="11" fill="#1f6a5a"/><rect x="30" y="10" width="94" height="14" fill="#1c8a2e"/></svg></div>
<div class="abs badge" style="left:243px;width:62px"><svg width="62" height="34"><circle cx="14" cy="19" r="12" fill="#f2c200"/><rect x="28" y="11" width="32" height="16" rx="2" fill="#d9d9d9"/></svg></div>
<div class="abs badge" style="left:325px;width:84px"><svg width="84" height="34"><rect x="1" y="4" width="82" height="26" fill="#fff" stroke="#cfcfcf"/><rect x="4" y="8" width="18" height="18" rx="3" fill="#5aa532"/></svg></div>

<div class="abs soc" style="left:650px;background:#35465c"></div>
<div class="abs soc" style="left:677px;background:#3b5998"></div>
<div class="abs soc" style="left:703px;background:#111"></div>
<div class="abs soc" style="left:730px;background:#2ea44f"></div>
<div class="abs soc" style="left:757px;background:#d9302a"></div>

<p class="abs copyright">Copyright © 2012 TalvoMesh. &nbsp;Privacy Policy &nbsp;/&nbsp; Terms and Conditions &nbsp;/&nbsp; Join Now &nbsp;/&nbsp; Browse Companies &nbsp;/&nbsp; How it Works</p>

</body>
</html>
```